Design a poster that illustrates the six central pillars of our school district's efforts with students. The attached PDF outlines the six main competencies we aim for students to possess upon graduation. Each of the 6 has 3 bullet points for the poster as well. The title is "Profile of a Kestrel". Our mascot is this attached winged wheel. The overall concept is that staff take kids when they are young and develop these 6 things when they graduate. Our colors are navy, red, and white. We will make this poster in a variety of sizes in offices, classrooms, and in digital spaces as well. On the PDF - ignore the column that says "Synthesis". That has nothing to do with this poster.

The district is Harlow Creek Public Schools https://www.harlowcreek-schools.example/

```html
<!DOCTYPE html>
<html lang="en">
<head>
<meta charset="utf-8">
<title>Profile of a Kestrel — Harlow Creek Public Schools</title>
<link href="https://fonts.googleapis.com/css2?family=Oswald:wght@400;500;600&display=swap" rel="stylesheet">
<style>
  :root {
    --navy: #0b1f63;
    --navy-deep: #071341;
    --red: #a31e24;
    --white: #ffffff;
    --stage: #505050;
  }
  * { box-sizing: border-box; margin: 0; padding: 0; }
  html, body { width: 1200px; height: 1001px; overflow: hidden; background: var(--stage); }
  .poster {
    position: absolute; left: 288px; top: 58px;
    width: 624px; height: 882px;
    background: var(--white);
    overflow: hidden;
    font-family: "Oswald", "Arial Narrow", sans-serif;
  }
  .poster-art { position: absolute; inset: 0; }
  .title {
    position: absolute; right: 52px; top: 52px;
    color: var(--white); text-align: right;
    font-weight: 600; font-size: 50px; line-height: 50px; letter-spacing: -0.5px;
    text-transform: uppercase;
  }
  .subtitle {
    position: absolute; right: 52px; top: 156px;
    color: var(--white); font-weight: 500; font-size: 12px; letter-spacing: 0.1px;
    text-transform: uppercase;
  }
  .mascot-name {
    position: absolute; left: 86px; top: 108px;
    display: flex; align-items: center; gap: 8px;
    color: var(--white); font-weight: 500; font-size: 26px;
  }
  .mascot-name .dot { width: 16px; height: 16px; border-radius: 50%; background: var(--red); }
  .pillar-name {
    position: absolute; color: var(--white);
    font-weight: 500; font-size: 21px; line-height: 30px; white-space: nowrap;
  }
  .pillar-points {
    position: absolute; left: 154px; width: 360px;
    color: var(--navy); font-size: 10.6px; line-height: 15px; font-weight: 400;
    list-style: none;
  }
  .site-url {
    position: absolute; right: 80px; top: 818px;
    color: var(--red); font-weight: 500; font-size: 27px;
  }
</style>
</head>
<body>
<main class="poster">
  <svg class="poster-art" viewBox="0 0 624 882" width="624" height="882" aria-hidden="true">
    <!-- header -->
    <polygon points="0,0 624,0 624,230 0,210" fill="var(--navy)"/>
    <polygon points="0,70 0,210 160,166" fill="var(--navy-deep)"/>
    <polygon points="0,62 0,76 468,212 478,194" fill="var(--red)"/>
    <!-- footer -->
    <polygon points="0,821 0,882 316,882" fill="var(--red)"/>

    <!-- connectors -->
    <g fill="none" stroke="var(--navy)" stroke-width="1.4">
      <polyline points="300,249 110,249 110,296"/>
      <polyline points="328,342 517,342 517,390"/>
      <polyline points="294,436 110,436 110,483"/>
      <polyline points="328,530 507,530 507,576"/>
      <polyline points="308,623 110,623 110,669"/>
    </g>

    <!-- banners -->
    <g fill="var(--red)">
      <polygon points="300,234 480,234 480,264 318,264"/>
      <polygon points="140,328 328,328 310,358 140,358"/>
      <polygon points="294,422 480,422 480,451 312,451"/>
      <polygon points="140,515 328,515 310,544 140,544"/>
      <polygon points="308,609 480,609 480,638 326,638"/>
      <polygon points="140,702 342,702 324,730 140,730"/>
    </g>

    <!-- badges -->
    <g>
      <g transform="translate(517,250)"><circle r="47" fill="var(--red)"/><circle r="43" fill="var(--white)"/><circle r="39" fill="var(--navy)"/></g>
      <g transform="translate(106,344)"><circle r="47" fill="var(--red)"/><circle r="43" fill="var(--white)"/><circle r="39" fill="var(--navy)"/></g>
      <g transform="translate(517,436)"><circle r="47" fill="var(--red)"/><circle r="43" fill="var(--white)"/><circle r="39" fill="var(--navy)"/></g>
      <g transform="translate(106,530)"><circle r="47" fill="var(--red)"/><circle r="43" fill="var(--white)"/><circle r="39" fill="var(--navy)"/></g>
      <g transform="translate(517,623)"><circle r="47" fill="var(--red)"/><circle r="43" fill="var(--white)"/><circle r="39" fill="var(--navy)"/></g>
      <g transform="translate(106,716)"><circle r="47" fill="var(--red)"/><circle r="43" fill="var(--white)"/><circle r="39" fill="var(--navy)"/></g>
    </g>

    <!-- icons -->
    <g fill="none" stroke="var(--white)" stroke-width="2" stroke-linecap="round" stroke-linejoin="round">
      <!-- speech bubbles -->
      <g transform="translate(517,250)">
        <rect x="-18" y="-16" width="24" height="16" rx="3"/><polyline points="-12,0 -14,7 -6,0"/>
        <rect x="-2" y="2" width="20" height="13" rx="3"/><polyline points="12,15 14,20 8,15"/>
      </g>
      <!-- gear -->
      <g transform="translate(106,344)">
        <circle r="9"/><circle r="3.5"/>
        <path d="M0,-15V-10M0,10V15M-15,0H-10M10,0H15M-10.6,-10.6L-7,-7M7,7L10.6,10.6M10.6,-10.6L7,-7M-7,7L-10.6,10.6"/>
      </g>
      <!-- clipboard -->
      <g transform="translate(517,436)">
        <rect x="-14" y="-18" width="28" height="36" rx="3"/><rect x="-6" y="-22" width="12" height="6" rx="2"/>
        <polyline points="-9,-8 -7,-6 -4,-10"/><line x1="0" y1="-8" x2="9" y2="-8"/>
        <polyline points="-9,0 -7,2 -4,-2"/><line x1="0" y1="0" x2="9" y2="0"/>
        <polyline points="-9,8 -7,10 -4,6"/><line x1="0" y1="8" x2="9" y2="8"/>
      </g>
      <!-- adapt arrows -->
      <g transform="translate(106,530)">
        <path d="M-14,-4A15,15 0 0 1 12,-8"/><polyline points="12,-16 12,-8 4,-8"/>
        <path d="M14,4A15,15 0 0 1 -12,8"/><polyline points="-12,16 -12,8 -4,8"/>
      </g>
      <!-- linked rings -->
      <g transform="translate(517,623)">
        <circle cx="-7" r="11"/><circle cx="7" r="11"/>
      </g>
      <!-- heart over hand -->
      <g transform="translate(106,716)">
        <path d="M0,2C-12,-6 -12,-17 -5,-17C-2,-17 0,-14 0,-12C0,-14 2,-17 5,-17C12,-17 12,-6 0,2Z"/>
        <path d="M-20,10C-12,8 -6,8 0,12H10M-20,18C-8,20 6,20 18,8"/>
      </g>
    </g>
  </svg>

  <h1 class="title">Profile<br>of a Kestrel</h1>
  <p class="subtitle">The six pillars of Harlow Creek Public Schools</p>
  <div class="mascot-name"><span class="dot"></span>Kestrel</div>

  <h2 class="pillar-name" style="left:332px;top:234px;">Communicator</h2>
  <ul class="pillar-points" style="top:269px;">
    <li>Expresses ideas clearly and respectfully (written &amp; verbal).</li>
    <li>Listens actively and understands diverse perspectives.</li>
    <li>Adjusts communication to suit the audience and context.</li>
  </ul>

  <h2 class="pillar-name" style="left:168px;top:328px;">Critical Thinker</h2>
  <ul class="pillar-points" style="top:364px;width:330px;">
    <li>Questions, analyzes, and evaluates information from multiple sources.</li>
    <li>Identifies and solves complex problems creatively.</li>
    <li>Uses evidence and diverse perspectives to form reasoned conclusions and make informed decisions</li>
  </ul>

  <h2 class="pillar-name" style="left:346px;top:422px;">Responsible</h2>
  <ul class="pillar-points" style="top:455px;">
    <li>Takes ownership of actions, choices, and commitments.</li>
    <li>Manages time, resources, and self to meet expectations.</li>
    <li>Acts with integrity and advocates for self and others.</li>
  </ul>

  <h2 class="pillar-name" style="left:172px;top:515px;">Adaptable</h2>
  <ul class="pillar-points" style="top:550px;width:340px;">
    <li>Responds productively to new situations, challenges, and feedback.</li>
    <li>Learns from new experiences and applies prior knowledge in evolving contexts.</li>
    <li>Adjusts behavior and approach to effectively engage with diverse groups and environments.</li>
  </ul>

  <h2 class="pillar-name" style="left:350px;top:609px;">Collaborator</h2>
  <ul class="pillar-points" style="top:645px;">
    <li>Contributes effectively and cooperatively to shared goals.</li>
    <li>Listens actively and values diverse ideas and perspectives.</li>
    <li>Engages respectfully, compromising and leading when appropriate.</li>
  </ul>

  <h2 class="pillar-name" style="left:172px;top:701px;">Compassionate</h2>
  <ul class="pillar-points" style="top:738px;width:350px;">
    <li>Understands and acknowledges others' feelings, perspectives, and experiences.</li>
    <li>Responds with kindness, patience, and support.</li>
    <li>Seeks to connect with and contribute positively to the well-being of others and the community.</li>
  </ul>

  <p class="site-url">harlowcreek-schools.example</p>
</main>
</body>
</html>
```